依頼概要
◆本のタイトル
港町グラス日記~灯りの奥のササヤキ~

◆著者
桑原 美津江

◆依頼目的/概要
電子書籍を出版しますので、表紙デザイン作成をお願いいたします。

◆デザイン要望
基本的にお任せです。
イラストや写真等素材を使用される場合には、
商用利用可の素材をお願いします。

色合い、デザイン、レイアウトともデザイナーさんにお任せしたいと思います。

※参考として書籍の原稿を添付します。

◆本の内容
ショットバー”ブルクハルモン”のオーナーバーテンダーである私、桑原美津江が実話をもとに店で繰り広げられる様々な人間ドラマを本にしました。
登場人物であるお客様をヒーロー、ヒロインにするつもりで構成しました。
読者が元気や活力を得て、人生を前向きに生きる一助になることを願い、書き進めました。バーという非日常の空間の中で、臨場感や私とお客様とのやりとりがダイレクトに伝わり、読者の様々な感情を揺さぶることができれば、嬉しく思います。

◆読者ターゲット層
〇30代、40代、50代前半までの働く男性、女性
〇自分の生き方や仕事に漠然とした不安や悩みがある人
〇人生を前向きに自分らしく生きたい人
〇職場間、夫婦間、親子間など人間関係にストレスや問題を抱えている人

◆デザイン要望
〇私が女性バーテンダーで、女性のご来店も多いので、女性が一人でも行ってみたいと思わせる雰囲気のデザイン希望です

〇バーというと敷居が高く、入りにくいイメージを持っている人が多いので、品位は保ちつつもあたたかい雰囲気が伝わるようにしていただきたいです

◆写真素材購入の際は別途写真代をお支払いします。その場合は電子書籍ですので、小サイズで結構です。

◆選定確約です。

◆選定デザインの他に、次点、次々点の方にも報酬をご用意しています。

◆その他、デザインに必要な情報がありましたら、お答えします。
遠慮なく聞いてください。
お盆中で、デザイナーさんから締め切り延長のご希望がありましたので、
2日間だけ、延長することになりました。よろしくお願いします。
■ 選んだ理由

赤、黒、白のデザインは、店と私の雰囲気にぴったりで、とても気に入りました。
オビも読者目線で考えていただき、感謝しています。
おしゃれで元気にもになるそんなデザインに感じました。

■ 提案者全員のお礼・コメント

原稿を読んでくださり、それぞれの強い思いでデザインを考えてくださったのが、
伝わってきました。
お一人、お一人に感謝申し上げます。
良いデザインばかりで、選ぶのに正直とても迷いました。
出版の機会がありましたら、またコンペにご参加くださるとありがたいです。
本当にありがとうございました。

```html
<!DOCTYPE html>
<html lang="ja">
<head>
<meta charset="utf-8">
<title>港町グラス日記〜灯りの奥のササヤキ〜</title>
<link rel="stylesheet" href="https://fonts.googleapis.com/css2?family=Shippori+Mincho:wght@600;800&family=Noto+Sans+JP:wght@500;700&display=swap">
<style>
  :root {
    --cream: #f4efe1;
    --ink: #2a2622;
    --accent: #e07b1f;
    --forest: #1d3a2c;
    --white: #ffffff;
    --photo-dark: #173a3a;
    --photo-warm: #e9a233;
  }
  * { margin: 0; padding: 0; box-sizing: border-box; }
  html, body { width: 750px; height: 1200px; overflow: hidden; background: var(--cream); }
  .cover { position: relative; width: 750px; height: 1200px; overflow: hidden; background: var(--cream); }

  .cocktail-photo {
    position: absolute; left: 0; top: 0; width: 605px; height: 845px;
    background: linear-gradient(180deg, var(--photo-dark) 0%, #2f4a3a 38%, #b7661f 58%, var(--photo-warm) 100%);
  }
  .subtitle {
    position: absolute; left: 566px; top: 236px;
    writing-mode: vertical-rl;
    font-family: "Shippori Mincho", serif; font-weight: 600;
    font-size: 27px; letter-spacing: 1px; line-height: 1; color: var(--white);
    white-space: nowrap;
  }
  .author {
    position: absolute; left: 22px; top: 708px;
    font-family: "Shippori Mincho", serif; font-weight: 800;
    font-size: 34px; letter-spacing: 3px; color: var(--white);
  }

  .title {
    position: absolute; left: 605px; top: 0; width: 145px; height: 845px;
    font-family: "Shippori Mincho", serif; font-weight: 800;
    color: var(--ink); line-height: 1; text-align: center;
  }
  .title .group { position: absolute; left: 0; width: 145px; }
  .title .char { display: block; }
  .title .place { top: 14px; font-size: 100px; }
  .title .place .char { height: 104px; }
  .title .glass { top: 262px; font-size: 96px; color: var(--accent); }
  .title .glass .char { height: 100px; }
  .title .diary { top: 620px; font-size: 100px; }
  .title .diary .char { height: 104px; }

  .obi {
    position: absolute; left: 0; top: 845px; width: 750px; height: 355px;
    background: var(--forest);
  }
  .obi-lead {
    position: absolute; left: 22px; top: 28px;
    font-family: "Noto Sans JP", sans-serif; font-weight: 700;
    font-size: 21.5px; color: var(--white); white-space: nowrap;
  }
  .bartender-photo {
    position: absolute; left: 0; top: 80px; width: 232px; height: 275px;
    background: linear-gradient(160deg, #3d4a44 0%, #6b5a45 55%, #2a3530 100%);
  }
  .obi-message {
    position: absolute; left: 245px; top: 92px;
    font-family: "Shippori Mincho", serif; font-weight: 800;
    font-size: 54px; line-height: 1.36; color: var(--white); white-space: nowrap;
  }
</style>
</head>
<body>
  <div class="cover">
    <div class="cocktail-photo" role="img" aria-label="カウンターに並ぶ色とりどりのカクテルグラスの写真"></div>
    <p class="subtitle">〜灯りの奥のササヤキ〜</p>
    <p class="author">桑原 美津江</p>

    <h1 class="title" aria-label="港町グラス日記">
      <span class="group place"><span class="char">港</span><span class="char">町</span></span>
      <span class="group glass"><span class="char">グ</span><span class="char">ラ</span><span class="char">ス</span></span>
      <span class="group diary"><span class="char">日</span><span class="char">記</span></span>
    </h1>

    <section class="obi">
      <p class="obi-lead">実在するショットバーでの交流を元に描いたヒューマンストーリー</p>
      <div class="bartender-photo" role="img" aria-label="バーカウンターに立つ女性バーテンダーの写真"></div>
      <p class="obi-message">いつの日かあなたに<br>お会いできる日を<br>楽しみにしています</p>
    </section>
  </div>
</body>
</html>
```